Label Design Refresh for existing High End Supplement line

Design a label for our high end supplement brand, packaged in a Cobal Blue bottle.... using Clear labels as the label stock media.

A clear label design will take advantage of the blue bottle and can incorporate any design element you create, metalic elements, new graphics etc.

our line spans 50 different product categories and over 400 unique SKUs, so any elements you suggest to differentiate products or categories will be appreciated.

see: www.quillantheralife.com
Updates

Need designers to meet project requirements. Full label, clear label stock design (clear background with exception for design elements and text etc.)

Target Market(s)

Men and Women 25-55 Health conscious and not price sensitive. Product is 5x higher cost than competition.

Industry/Entity Type

Sexual health for men and women. testosterone, hormone health, nootropics

Font styles to use
Sans Serif

Colors

Designer to choose colors to be used in the design.

Requirements
Must have
• Clear label design for Cobalt blue, packer style, pharma bottle. Must feature Velmora brand on front panel. Must show entire label panel design as 2.8in x 7.25in. Graphics can be full color with metalic or foil type elements.
Nice to have
• Name of products include: SHBG, Testosterone & Libido, Adrenal Support Phase 2, LH Formula, ADHD Phase1,
Should not have
• Busy designs that are stock images for supplement label layouts

```html
<!DOCTYPE html>
<html lang="en">
<head>
<meta charset="utf-8">
<title>Velmora SHBG Label</title>
<link href="https://fonts.googleapis.com/css2?family=Questrial&family=Roboto:ital,wght@0,500;0,700;0,900;1,400&display=swap" rel="stylesheet">
<style>
  :root{
    --stage:#4a4b4d;
    --label-light:#eef3fa;
    --label-blue:#c9dbf2;
    --brand-blue:#2f49a8;
    --cap-blue:#2a3fa0;
    --green:#5cb547;
    --ink:#2b2f3a;
    --silver-a:#e9eaec;
    --silver-b:#a9acb2;
  }
  *{margin:0;padding:0;box-sizing:border-box}
  html,body{width:1200px;height:900px;overflow:hidden;background:var(--stage)}
  .label{
    position:absolute;left:50px;top:238px;width:1100px;height:424px;
    background:linear-gradient(100deg,var(--label-light) 0%,#f4f7fc 45%,var(--label-blue) 100%);
    font-family:"Questrial",sans-serif;color:var(--ink);overflow:hidden;
  }
  .brand-strip{
    position:absolute;left:0;top:0;width:100px;height:100%;
    background:linear-gradient(90deg,var(--silver-b),var(--silver-a) 40%,#f7f7f8 55%,var(--silver-b));
  }
  .brand-strip .brand-name{
    position:absolute;left:50px;top:160px;transform:translate(-50%,-50%) rotate(-90deg);
    font-family:"Roboto",sans-serif;font-weight:900;font-size:52px;color:#16171a;white-space:nowrap;
  }
  .count-badge{
    position:absolute;left:16px;top:325px;width:84px;height:95px;background:var(--cap-blue);color:#fff;
    text-align:center;padding-top:6px;
  }
  .count-badge .num{font-size:52px;line-height:54px}
  .count-badge .unit{font-size:10px;letter-spacing:1px;line-height:11px}
  .pattern{
    position:absolute;right:0;top:0;width:260px;height:100%;
    background:radial-gradient(circle at 70% 50%,#aac5ea 0%,rgba(201,219,242,.4) 60%,rgba(238,243,250,0) 100%);
  }
  .title{position:absolute;left:137px;top:74px;font-family:"Roboto",sans-serif;font-weight:700;font-size:84px;color:var(--brand-blue);letter-spacing:-1px}
  .subtitle{position:absolute;left:139px;top:160px;font-size:26px;color:var(--green);letter-spacing:3px}
  .benefits{position:absolute;left:158px;top:238px;font-family:"Roboto",sans-serif;font-style:italic;font-size:17px;line-height:21.5px;letter-spacing:.8px;list-style:disc}
  .category{position:absolute;left:139px;top:385px;font-size:14px;letter-spacing:2px}
  .info{position:absolute;left:500px;top:28px;width:334px;font-size:13px;line-height:16.3px;text-align:justify}
  .info p{margin-bottom:13px}
  .disclaimer{border:1.5px solid var(--ink);border-radius:4px;padding:6px 9px;font-size:12px;line-height:15.5px;letter-spacing:.6px;text-align:justify}
  .sign-off{position:absolute;left:500px;top:300px;width:220px}
  .sign-off .brand-name{font-family:"Roboto",sans-serif;font-weight:900;font-size:27px;color:var(--brand-blue)}
  .sign-off .web{font-size:13px}
  .icons{position:absolute;left:722px;top:300px}
  .distributor{position:absolute;left:500px;top:353px;width:258px;font-size:11px;line-height:12.5px;text-align:justify}
  .distributor b{font-weight:normal;font-size:12px;display:block;margin-bottom:2px}
</style>
</head>
<body>
<section class="label">
  <div class="pattern" role="img" aria-label="Soft blue molecular hexagon pattern"></div>
  <div class="brand-strip">
    <div class="brand-name">VELMORA</div>
    <div class="count-badge"><div class="num">60</div><div class="unit">VEGETABLE<br>CAPSULES</div></div>
  </div>
  <h1 class="title">SHBG</h1>
  <div class="subtitle">MENS FORMULA</div>
  <ul class="benefits">
    <li>Testosterone &amp; Libido</li>
    <li>Adrenal Support Phase 2</li>
    <li>LH Formula</li>
    <li>ADHD Phase1</li>
  </ul>
  <div class="category">DIETARY SUPPLEMENT</div>
  <div class="info">
    <p>DIRECTIONS: Lorem ipsum dolor sit amet, consectetuer adipiscing elit, sed diam nonummy nibh euismod tincidunt ut laoreet dolore magna aliquam erat volutpat.</p>
    <p>WARNINGS: Lorem ipsum dolor sit amet, consectetuer adipiscing elit, sed diam nonummy nibh euismod tincidunt ut laoreet dolore magna aliquam erat volutpat.</p>
    <div class="disclaimer">THESE STATEMENTS HAVE NOOT BEEN EVALUATED BY THE FOOD AND DRUG ADMINISTRATION. THIS PRODUCT IS NOT INTENDED TO DIAGNOSE, TREET, CURE OR PREVENT ANY DISEASE.</div>
  </div>
  <div class="sign-off">
    <div class="brand-name">VELMORA</div>
    <div class="web">www.quillantheralife.com</div>
  </div>
  <svg class="icons" width="110" height="40" viewBox="0 0 110 40" fill="none" stroke="#16171a" stroke-width="2" role="img" aria-label="Disposal and material marks">
    <circle cx="20" cy="6" r="3" fill="#16171a"/>
    <path d="M20 10v14M20 24l-3 10M20 24l3 10M20 14l-6 6"/>
    <path d="M4 20h9l-1 14H5z"/>
    <circle cx="56" cy="20" r="11"/>
    <path d="M95 8l10 18H85z"/>
    <text x="95" y="37" font-size="6" fill="#16171a" stroke="none" text-anchor="middle" font-family="Roboto,sans-serif">PETE</text>
  </svg>
  <div class="distributor"><b>Distributed by:</b>Lorem ipsum dolor sit amet, consectetuer adipiscing elit, sed diam nonummy nibh euismod tincidunt ut laoreet</div>
</section>
</body>
</html>
```